Lead Sales Portal Needs to Generate B2B Signup's

We are looking for banner ad designs to drive new business (B2B) traffic to our insurance and mortgage industry self serve lead sites. The sites are HomeLoanProspectHub.com and PolicyBuyerHub.com, and we service over 45,000 insurance agents and mortgage lenders in a self serve lead portal model. We want our banners to generate more of these clients.

Our clients come to our sites, browse our database and then pick out and purchase the consumer leads that they need to generate new business.

We advertise extensively on Zyntrix and on other PPC platforms, and our existing banners are looking really tired.

Some of the ad copy that works well for us is:

Cherry Pick Your Life Leads - Why Pay More Than $3.50 For Life Insurance Leads?
Sign up today and we'll match up to $250

Agents - Here's $250 For New Clients. Cherry Pick Your Life Insurance Leads & Save! Sign up today and we'll match up to $250

One of our Landing Pages that performs well is here:
http://www.policybuyerhub.com/lp/008/

One of our competitors ad's are here:

http://www.brellow.com/search/results?q=QuoteMarten&ad=427360

We're looking for a design that is eye catching, uses our "Deeply Discounted Leads" and our "$250 match bonus"

This is the second contest that we have for the same sites. The previous designs were great and really performed well, so we are looking for new designs now that 6 months have passed. I have uploaded some winning banners from the last group for your information.

Reason: I've been asked by some of the designers to delay a day to get their designs in. I'm happy to do it!

Target Market(s)

These are insurance agents and mortgage lenders. All of our clients are business' or individuals within the business. This is a B2B campaign, so we need something that is professional and upscale. These are NOT consumer facing ad's!

Industry/Entity Type

Insurance

Font styles to use
Sans Serif

Requirements
Must have
• We must have the logos for the sites in the banners. Also, we must have a call to action arrow and "Go" button. Some animation is necessary, (especially around the arrow and the GO button).

One or two designs.

File type

.JPEG
.JPG
.PNG
.GIF

File size

150 KB or smaller

Image sizes

Vertical rectangle: 240 x 400
Mobile leaderboard: 320 x 50
Banner: 468 x 60
Leaderboard: 728 x 90
Square: 250 x 250
Small square: 200 x 200
Large rectangle: 336 x 280
Inline rectangle: 300 x 250
Skyscraper: 120 x 600
Wide skyscraper: 160 x 600
Half-page: 300 x 600
Large leaderboard: 970 x 90

```html
<!DOCTYPE html>
<html lang="en">
<head>
<meta charset="utf-8">
<title>Policy Buyer Hub – Agent Signup Banners</title>
<link href="https://fonts.googleapis.com/css2?family=Arimo:wght@700&family=Open+Sans:wght@400;600&display=swap" rel="stylesheet">
<style>
:root{
  --board-top:#f7f7f7;
  --board-bottom:#b9b9b9;
  --ink:#161616;
  --panel:#f4f4f4;
  --headline:#3a3a3a;
  --green:#7b9a1c;
  --lime:#c4e02a;
  --btn-top:#b3d143;
  --btn-bottom:#6d8e14;
  --rule:#b5b5b5;
  --white:#ffffff;
  --sub:#dfe8ee;
  --photo-a:#e9ebec;
  --photo-b:#2a2c30;
}
*{box-sizing:border-box;margin:0;padding:0}
html,body{width:1200px;height:1000px;overflow:hidden}
body{background:linear-gradient(180deg,var(--board-top),var(--board-bottom));position:relative;font-family:"Open Sans",Arial,sans-serif}
.banner{position:absolute;overflow:hidden;background:var(--panel);box-shadow:10px 12px 14px rgba(0,0,0,.45)}
.head{font-family:"Arimo",Arial,sans-serif;font-weight:700;text-transform:uppercase;color:var(--headline);text-align:center;position:absolute;line-height:1}
.green{color:var(--green)}
.brand{position:absolute;display:flex;align-items:center;gap:8px;color:var(--white);font-family:"Open Sans",Arial,sans-serif;font-weight:400;white-space:nowrap}
.brand .dot{border-radius:50%;background:var(--white);flex:none}
.band{position:absolute;background:var(--ink)}
.pitch{position:absolute;color:var(--sub);text-align:center;line-height:1.2}
.go{position:absolute;border-radius:22px;background:linear-gradient(180deg,var(--btn-top),var(--btn-bottom));border:2px solid #d9ec8a;color:var(--white);font-family:"Open Sans",Arial,sans-serif;font-weight:600;display:flex;align-items:center;justify-content:center;gap:12px}
.go .arrow-ico{border-radius:50%;background:var(--white);display:flex;align-items:center;justify-content:center}
.photo{position:absolute}

/* square */
.banner--square{left:391px;top:315px;width:480px;height:398px}
/* skyscraper */
.banner--sky{left:930px;top:114px;width:212px;height:799px}
/* leaderboard */
.banner--leader{left:63px;top:815px;width:808px;height:98px}
</style>
</head>
<body>

<!-- Square banner -->
<section class="banner banner--square">
  <svg class="photo" width="480" height="330" viewBox="0 0 480 330" role="img" aria-label="Photo of two smiling young business professionals in dark suits">
    <defs>
      <linearGradient id="sqPhoto" x1="0" y1="0" x2="0" y2="1">
        <stop offset="0" stop-color="var(--photo-a)"/><stop offset="1" stop-color="var(--photo-b)"/>
      </linearGradient>
    </defs>
    <rect width="480" height="330" fill="url(#sqPhoto)"/>
    <path d="M194,0 Q300,165 245,330 L480,330 L480,0 Z" fill="var(--panel)"/>
    <path d="M194,0 Q300,165 245,330" fill="none" stroke="var(--rule)" stroke-width="5"/>
    <path d="M194,0 L480,0 L480,57 L226,57 Q212,25 194,0 Z" fill="var(--ink)"/>
  </svg>
  <div class="brand" style="left:258px;top:9px;font-size:19px"><span class="dot" style="width:32px;height:32px"></span>Policy Buyer Hub</div>
  <div class="head green" style="left:262px;top:74px;width:218px;font-size:45px">Agents!</div>
  <div class="head" style="left:262px;top:124px;width:218px;font-size:22px;line-height:1.1">Here's $250 for<br>new clients</div>
  <div style="position:absolute;left:300px;top:184px;width:150px;height:2px;background:var(--rule);box-shadow:0 2px 4px rgba(0,0,0,.25)"></div>
  <div class="head" style="left:262px;top:200px;width:218px;font-size:22px;line-height:1.2">Cherry pick<br>your life</div>
  <div class="head green" style="left:262px;top:253px;width:218px;font-size:30px">Insurance</div>
  <div class="head" style="left:262px;top:289px;width:218px;font-size:27px;color:#2c2c2c">Leads &amp; save!</div>
  <div class="band" style="left:0;top:330px;width:480px;height:68px"></div>
  <div class="pitch" style="left:20px;top:336px;width:250px;font-size:19px">Sign up today and we'll<br>match up to $250</div>
  <svg style="position:absolute;left:255px;top:352px" width="70" height="30" viewBox="0 0 70 30"><path d="M4,22 Q32,30 58,12" fill="none" stroke="#fff" stroke-width="3" stroke-linecap="round"/><path d="M48,8 L60,11 L55,22" fill="none" stroke="#fff" stroke-width="3" stroke-linecap="round" stroke-linejoin="round"/></svg>
  <div class="go" style="left:331px;top:343px;width:124px;height:43px;font-size:26px">GO<span class="arrow-ico" style="width:22px;height:22px"><svg width="12" height="12" viewBox="0 0 12 12"><path d="M1,6 H8 M5,2 L9,6 L5,10" stroke="#6d8e14" stroke-width="2.4" fill="none"/></svg></span></div>
</section>

<!-- Skyscraper banner -->
<section class="banner banner--sky">
  <div class="band" style="left:0;top:0;width:212px;height:61px"></div>
  <div class="brand" style="left:6px;top:13px;font-size:19px;gap:7px"><span class="dot" style="width:34px;height:34px"></span>Policy Buyer Hub</div>
  <div class="head green" style="left:0;top:72px;width:212px;font-size:43px">Agents!</div>
  <div class="head" style="left:0;top:119px;width:212px;font-size:22px;line-height:1.1">Here's $250 for<br>new clients</div>
  <svg class="photo" style="left:0;top:168px" width="212" height="318" viewBox="0 0 212 318" role="img" aria-label="Photo of two smiling young business professionals in dark suits">
    <defs>
      <linearGradient id="skyPhoto" x1="0" y1="0" x2="0" y2="1">
        <stop offset="0" stop-color="var(--photo-a)"/><stop offset="1" stop-color="var(--photo-b)"/>
      </linearGradient>
    </defs>
    <path d="M0,22 Q106,-12 212,22 L212,296 Q106,330 0,296 Z" fill="url(#skyPhoto)"/>
    <path d="M0,22 Q106,-12 212,22 M0,296 Q106,330 212,296" fill="none" stroke="var(--rule)" stroke-width="4"/>
  </svg>
  <div class="head" style="left:0;top:494px;width:212px;font-size:24px;line-height:1.2">Cherry pick<br>your life</div>
  <div class="head green" style="left:0;top:552px;width:212px;font-size:28px">Insurance</div>
  <div class="head green" style="left:0;top:586px;width:212px;font-size:26px">Leads &amp; save!</div>
  <div class="band" style="left:0;top:626px;width:212px;height:173px"></div>
  <div class="pitch" style="left:0;top:634px;width:212px;font-size:22px;line-height:1.1">Sign up today<br>and we'll match<br>up to $250</div>
  <svg style="position:absolute;left:166px;top:688px" width="34" height="48" viewBox="0 0 34 48"><path d="M26,4 Q30,30 8,40" fill="none" stroke="#fff" stroke-width="3" stroke-linecap="round"/><path d="M8,28 L6,41 L18,44" fill="none" stroke="#fff" stroke-width="3" stroke-linecap="round" stroke-linejoin="round"/></svg>
  <div class="go" style="left:40px;top:736px;width:132px;height:45px;font-size:29px">GO<span class="arrow-ico" style="width:24px;height:24px"><svg width="13" height="13" viewBox="0 0 12 12"><path d="M1,6 H8 M5,2 L9,6 L5,10" stroke="#6d8e14" stroke-width="2.4" fill="none"/></svg></span></div>
</section>

<!-- Leaderboard banner -->
<section class="banner banner--leader">
  <svg class="photo" style="left:0;top:0" width="808" height="98" viewBox="0 0 808 98" role="img" aria-label="Photo of two smiling young business professionals in dark suits">
    <defs>
      <linearGradient id="ldPhoto" x1="0" y1="0" x2="0" y2="1">
        <stop offset="0" stop-color="var(--photo-a)"/><stop offset="1" stop-color="var(--photo-b)"/>
      </linearGradient>
    </defs>
    <path d="M205,0 L440,0 Q415,49 440,98 L205,98 Q188,49 205,0 Z" fill="url(#ldPhoto)"/>
    <path d="M205,0 Q188,49 205,98" fill="none" stroke="var(--rule)" stroke-width="4"/>
    <path d="M420,0 L808,0 L808,98 L420,98 Q404,49 420,0 Z" fill="var(--ink)"/>
  </svg>
  <div class="head green" style="left:0;top:12px;width:200px;font-size:34px">Agents!</div>
  <div class="head" style="left:0;top:46px;width:200px;font-size:19px;line-height:1.05">Here's $250 for<br>new clients</div>
  <div class="head" style="left:428px;top:9px;width:240px;font-size:16.5px;line-height:1.2;color:var(--lime)">Cherry pick your life<br>insurance leads &amp; save!</div>
  <div class="brand" style="left:660px;top:17px;font-size:14px;gap:5px"><span class="dot" style="width:22px;height:22px"></span>Policy Buyer Hub</div>
  <div class="pitch" style="left:438px;top:52px;width:200px;font-size:14.5px;line-height:1.4">Sign up today and we'll<br>match up to $250</div>
  <svg style="position:absolute;left:624px;top:70px" width="56" height="20" viewBox="0 0 56 20"><path d="M3,14 Q26,20 48,9" fill="none" stroke="#fff" stroke-width="2.5" stroke-linecap="round"/><path d="M40,5 L50,8 L45,16" fill="none" stroke="#fff" stroke-width="2.5" stroke-linecap="round" stroke-linejoin="round"/></svg>
  <div class="go" style="left:685px;top:51px;width:98px;height:34px;font-size:21px;gap:10px">GO<span class="arrow-ico" style="width:18px;height:18px"><svg width="10" height="10" viewBox="0 0 12 12"><path d="M1,6 H8 M5,2 L9,6 L5,10" stroke="#6d8e14" stroke-width="2.4" fill="none"/></svg></span></div>
</section>

</body>
</html>
```